Online video and marketing company business cards

Need to get some new business cards designed to fit with our new logo. The cards should be professional, clean and simple.

Cards should have:

Name
Position
2 line address
telephone
mobile
email address
web address

We need to have our logo and if possible say what we do...
ONLINE FILM PRODUCTION & STRATEGY

Marketing

```html
<!DOCTYPE html>
<html lang="en">
<head>
<meta charset="utf-8">
<title>Reelwave Stationery</title>
<link href="https://fonts.googleapis.com/css2?family=Cabin:wght@400;600&family=Arimo:wght@400&family=Cormorant+Garamond:ital@1&display=swap" rel="stylesheet">
<style>
  :root{
    --navy:#0b4468;
    --sky:#6fa5c4;
    --paper:#ffffff;
    --backdrop:#e6e8ea;
    --ink:#0b4468;
  }
  *{box-sizing:border-box;margin:0;padding:0}
  html,body{width:1200px;height:933px;overflow:hidden;background:var(--backdrop)}
  .canvas{position:relative;width:1200px;height:933px}

  .brand{font-family:"Cabin",sans-serif;font-weight:600;color:var(--navy);display:flex;align-items:center;gap:8px;letter-spacing:-.5px}
  .brand-dot{border-radius:50%;background:var(--navy);display:inline-block}

  /* Letterhead */
  .letterhead{position:absolute;left:40px;top:46px;width:640px;height:840px;background:var(--paper);box-shadow:0 2px 10px rgba(0,0,0,.18);overflow:hidden}
  .letterhead .brand{position:absolute;left:0;right:0;top:70px;justify-content:center;font-size:40px}
  .letterhead .brand-dot{width:26px;height:26px}
  .letter-body{position:absolute;left:80px;right:70px;top:205px;font-family:"Cabin",sans-serif;font-size:13.5px;line-height:1.38;color:var(--ink);text-align:justify}
  .letter-body p+p{margin-top:18px}
  .signoff{position:absolute;right:80px;top:528px;font-family:"Cormorant Garamond",serif;font-style:italic;font-size:28px;line-height:1;color:var(--navy)}
  .corner-ring{position:absolute;left:-110px;bottom:-100px}
  .letter-contact{position:absolute;left:80px;bottom:48px;font-family:"Arimo",sans-serif;font-size:11.5px;line-height:1.4;color:var(--navy)}
  .letter-contact .group+.group{margin-top:8px}

  .line{display:flex;align-items:center;gap:5px}
  .icon{width:11px;height:11px;flex:none}

  /* Cards */
  .card{position:absolute;width:480px;height:274px;box-shadow:0 2px 10px rgba(0,0,0,.2);overflow:hidden}
  .card-front{left:700px;top:130px;background:var(--paper)}
  .card-back{left:700px;top:450px;background:var(--navy);display:flex;flex-direction:column;align-items:center;justify-content:center;gap:40px}

  .card-front .brand{position:absolute;left:36px;top:90px;font-size:28px}
  .card-front .brand-dot{width:18px;height:18px}
  .holder{position:absolute;right:36px;top:40px;text-align:right;font-family:"Cabin",sans-serif}
  .holder-name{font-size:19px;color:var(--navy)}
  .holder-role{font-size:13px;color:var(--sky)}
  .phones{position:absolute;left:180px;top:160px;font-family:"Arimo",sans-serif;font-size:12.5px;line-height:1.45;color:var(--navy)}
  .details{position:absolute;right:36px;top:140px;font-family:"Arimo",sans-serif;font-size:12.5px;line-height:1.45;color:var(--navy)}
  .card-ring{position:absolute;left:-40px;bottom:-150px}

  .back-mark{width:110px;height:110px;border-radius:50%;border:14px solid var(--sky)}
  .tagline{font-family:"Arimo",sans-serif;font-size:14px;letter-spacing:.3px;color:#ffffff;text-transform:uppercase}
</style>
</head>
<body>
<main class="canvas">

  <section class="letterhead" aria-label="Letterhead">
    <div class="brand"><span class="brand-dot"></span>reelwave</div>

    <div class="letter-body">
      <p>Lorem ipsum dolor sit amet, consectetur adipiscing elit. Cras id urna nisl. Etiam laoreet placerat urna ut lobortis. Mauris non tellus egestas, faucibus nisi in, luctus lorem. Praesent porttitor nisl non nunc volutpat rhoncus. Nunc suscipit volutpat felis, eget facilisis quam porttitor sit amet. Aenean venenatis viverra arcu et blandit. Etiam id sapien vehicula, ullamcorper leo at, gravida lorem. Integer nec diam consequat, pellentesque nibh sed, faucibus neque. Nam vulputate eros nisi, vitae tempor quam facilisis nec. Duis euismod nulla in dui venenatis, non faucibus enim consectetur. Vestibulum semper bibendum faucibus. Quisque pellentesque nibh eget velit convallis, in tincidunt massa euismod.</p>
      <p>In hac habitasse platea dictumst. In accumsan mi at sapien aliquam congue. Nunc tristique semper aliquet. Etiam non auctor sapien. Donec cursus feugiat euismod orci, a euismod augue. Mauris porta nisi consectetur turpis tristique varius.</p>
    </div>

    <div class="signoff">sincerely</div>

    <svg class="corner-ring" width="380" height="380" viewBox="0 0 380 380" aria-hidden="true">
      <circle cx="190" cy="190" r="168" fill="none" stroke="var(--navy)" stroke-width="28"/>
    </svg>

    <div class="letter-contact">
      <div class="group">
        <div class="line"><svg class="icon" viewBox="0 0 12 12"><rect x="3" y="0.5" width="6" height="11" rx="1" fill="none" stroke="var(--navy)"/></svg>555.210.4417</div>
        <div class="line"><svg class="icon" viewBox="0 0 12 12"><path d="M2 1l3 0 1 3-1.5 1a7 7 0 0 0 3 3l1-1.5 3 1v3c-6 0-10-4-10-10z" fill="var(--navy)"/></svg>555.210.4418</div>
      </div>
      <div class="group">
        <div class="line"><svg class="icon" viewBox="0 0 12 12"><circle cx="6" cy="6" r="5" fill="none" stroke="var(--navy)"/><path d="M1 6h10M6 1c-3 3-3 7 0 10M6 1c3 3 3 7 0 10" fill="none" stroke="var(--navy)" stroke-width=".8"/></svg>www.reelwave.com</div>
        <div class="line"><svg class="icon" viewBox="0 0 12 12"><rect x="1" y="2.5" width="10" height="7" fill="var(--navy)"/></svg>hello@reelwave.com</div>
      </div>
    </div>
  </section>

  <section class="card card-front" aria-label="Business card front">
    <div class="holder">
      <div class="holder-name">Daniel Harper</div>
      <div class="holder-role">CEO/President</div>
    </div>
    <div class="brand"><span class="brand-dot"></span>reelwave</div>

    <div class="phones">
      <div class="line"><svg class="icon" viewBox="0 0 12 12"><rect x="3" y="0.5" width="6" height="11" rx="1" fill="none" stroke="var(--navy)"/></svg>555.210.4417</div>
      <div class="line"><svg class="icon" viewBox="0 0 12 12"><path d="M2 1l3 0 1 3-1.5 1a7 7 0 0 0 3 3l1-1.5 3 1v3c-6 0-10-4-10-10z" fill="var(--navy)"/></svg>555.210.4418</div>
    </div>

    <div class="details">
      <div class="line"><svg class="icon" viewBox="0 0 12 12"><circle cx="6" cy="6" r="5" fill="none" stroke="var(--navy)"/><path d="M1 6h10M6 1c-3 3-3 7 0 10M6 1c3 3 3 7 0 10" fill="none" stroke="var(--navy)" stroke-width=".8"/></svg>www.reelwave.com</div>
      <div class="line"><svg class="icon" viewBox="0 0 12 12"><rect x="1" y="2.5" width="10" height="7" fill="var(--navy)"/></svg>hello@reelwave.com</div>
      <div class="line"><svg class="icon" viewBox="0 0 12 12"><path d="M6 1l5 5h-1.5v5h-7v-5h-1.5z" fill="var(--navy)"/></svg>88 Harbor Lane</div>
      <div class="line"><span class="icon"></span>Riverton, ST 0420</div>
    </div>

    <svg class="card-ring" width="260" height="260" viewBox="0 0 260 260" aria-hidden="true">
      <circle cx="130" cy="130" r="110" fill="none" stroke="var(--navy)" stroke-width="22"/>
    </svg>
  </section>

  <section class="card card-back" aria-label="Business card back">
    <span class="back-mark" aria-hidden="true"></span>
    <p class="tagline">Online Film Production &amp; Strategy</p>
  </section>

</main>
</body>
</html>
```